Velvet Strut

The site will showcase the different drag queens of Manchester and provide an area for photography, video, social media feeds (such as zingo and Kinloop) as well as reviews of Drag queens to give the public a place to discuss shows or individuals.

Target Market(s)

Gay men

Industry/Entity Type

Media

Font styles to use
Decorative

Colors

Designer to choose colors to be used in the design.

Requirements
Must have
• Bright, bold, showbiz, glamorous but a little tacky at the same time.

```html
<!DOCTYPE html>
<html lang="en">
<head>
<meta charset="utf-8">
<title>Velvet Strut</title>
<link href="https://fonts.googleapis.com/css2?family=Alfa+Slab+One&family=Lobster&family=Open+Sans:wght@400;600;700&display=swap" rel="stylesheet">
<style>
:root{
  --ink:#333333;
  --dark:#2f2f2f;
  --pink:#f0105f;
  --page:#f6f6f6;
  --card:#ffffff;
  --text:#8a8a8a;
  --rule:#e4e4e4;
  --blue:#1fa5c9;
  --teal:#5aaa96;
  --placeholder:#ececec;
  --thumb:#555555;
}
*{box-sizing:border-box;margin:0;padding:0}
html,body{width:686px;height:1200px;overflow:hidden;background:var(--page)}
body{font-family:"Open Sans",Arial,sans-serif;color:var(--text)}
.page{position:relative;width:686px;height:1200px;overflow:hidden;background:var(--page)}

/* header */
.site-header{position:absolute;left:0;top:0;width:686px;height:98px;background:var(--ink);text-align:center}
.brand{position:absolute;left:0;right:0;top:20px;font-family:"Open Sans",Arial,sans-serif;font-weight:600;font-size:26px;line-height:32px;color:#ffffff;letter-spacing:1px}
.tagline{position:absolute;left:0;right:0;top:56px;font-family:"Lobster",cursive;font-size:16px;color:#8d8d8d}

/* nav */
.main-nav{position:absolute;left:0;top:98px;width:686px;height:29px;background:var(--pink)}
.main-nav ul{list-style:none;display:flex;position:absolute;left:57px;top:0;height:29px}
.main-nav li{font-family:"Alfa Slab One",Georgia,serif;font-size:8.5px;color:#fff;padding:0 10px;line-height:29px;position:relative}
.main-nav li.active::before{content:"";position:absolute;left:0;right:0;top:-2px;height:2px;background:#e8e8e8}
.search{position:absolute;left:521px;top:106px;width:108px;height:16px;background:#fff;display:flex;align-items:center;padding-left:5px;font-size:7px;color:#aaa}
.search svg{position:absolute;right:4px;top:3px}

/* hero */
.hero{position:absolute;left:56px;top:142px;width:573px;height:187px;background:linear-gradient(90deg,#c9a391 0%,#b67d6c 28%,#8e2a22 50%,#3a1412 72%,#151010 100%);border:1px solid #222}
.hero-caption{position:absolute;left:360px;top:150px;width:260px;height:79px;background:rgba(150,150,150,.72);padding:6px 9px}
.hero-caption h2{font-family:"Alfa Slab One",Georgia,serif;font-weight:400;font-size:14px;color:#3a3a3a;margin-bottom:3px}
.hero-caption p{font-size:8.5px;line-height:11px;color:#444}

/* sidebar */
.sidebar{position:absolute;left:56px;top:361px;width:134px}
.side-title{font-family:"Alfa Slab One",Georgia,serif;font-weight:400;font-size:8px;color:var(--pink);margin-bottom:12px}
.tweet{font-size:8.6px;line-height:10.6px;padding-bottom:4px;margin-bottom:5px;border-bottom:1px solid var(--rule)}
.tweet b{color:#777;font-weight:600}
.tweet time{display:block;font-size:7px;color:#aaa}
.events{margin-top:30px}
.event{font-size:8.6px;line-height:10.6px;padding-bottom:6px;margin-bottom:9px;border-bottom:1px solid var(--rule)}
.event:last-child{border-bottom:0}
.event h4{font-size:10px;color:var(--pink);font-weight:700;margin-bottom:1px}
.event a{color:var(--pink);font-weight:600;text-decoration:none}

/* cards */
.card{position:absolute;background:var(--card);padding:6px 8px}
.post-title{font-family:"Alfa Slab One",Georgia,serif;font-weight:400;font-size:7.5px;line-height:9px;color:var(--pink);margin-top:11px}
.post-date{font-size:7px;color:#999;margin-top:4px}
.post-body{font-size:8.6px;line-height:10.8px;margin-top:8px}
.post-meta{border-top:1px solid var(--rule);margin-top:12px;padding-top:10px;font-size:8.6px;line-height:11.5px}
.post-meta a{color:var(--pink);text-decoration:none}
.pic{display:flex;align-items:center;justify-content:center;width:114px;height:114px;font-family:"Alfa Slab One",Georgia,serif;font-size:17px;color:#fff}
.pic.blue{background:var(--blue)}
.pic.teal{background:var(--teal)}
.placeholder{width:100%;height:80px;background:var(--placeholder)}
.video{position:relative;width:100%;height:64px}
.video .bar{position:absolute;left:0;right:0;top:0;height:10px;background:rgba(0,0,0,.55);font-size:6.5px;color:#fff;padding-left:16px;line-height:10px;white-space:nowrap;overflow:hidden}
.video .controls{position:absolute;left:0;right:0;bottom:0;height:10px;background:#222;font-size:5.5px;color:#ddd;line-height:10px;padding-left:34px}
.video svg{position:absolute;left:50%;top:50%;transform:translate(-50%,-50%)}

.load-more{position:absolute;left:350px;top:959px;width:132px;height:21px;background:var(--blue);border:1px solid #168aab;color:#fff;font-size:8.5px;text-align:center;line-height:19px}

/* footer */
.site-footer{position:absolute;left:0;top:1020px;width:686px;height:162px;background:var(--dark);color:#ddd}
.foot-title{font-family:"Alfa Slab One",Georgia,serif;font-weight:400;font-size:7.5px;color:#aaa;letter-spacing:.3px;margin-bottom:11px}
.foot-col{position:absolute;top:20px}
.foot-links{list-style:none;font-size:8.6px;line-height:10.2px;color:#eee}
.foot-text p{font-size:8.6px;line-height:10.4px;color:#eee}
.thumbs{display:grid;grid-template-columns:repeat(4,34px);column-gap:15px;row-gap:16px}
.thumbs span{width:34px;height:34px;background:var(--thumb);display:block}
.socials{display:flex;gap:6px}
.social{display:flex;flex-direction:column;align-items:center;gap:3px;font-size:6.5px;color:#ccc}
.social i{display:block;width:19px;height:19px;border-radius:50%}
.social.one i{background:#20a9e0}
.social.two i{background:#1e5bb8}
.social.three i{background:#d62a1f}
.bottom-bar{position:absolute;left:0;top:1182px;width:686px;height:18px;background:var(--pink);color:#fff;font-size:7px;line-height:18px}
.bottom-bar .copy{position:absolute;left:56px}
.bottom-bar .policy{position:absolute;right:64px}
</style>
</head>
<body>
<div class="page">

  <header class="site-header">
    <div class="brand">Velvet Strut</div>
    <div class="tagline">Lorem ipsum dolor sit amet.</div>
  </header>

  <nav class="main-nav">
    <ul>
      <li class="active">MAIN PAGE</li>
      <li>ABOUT US</li>
      <li>BLOG</li>
      <li>PHOTOS</li>
      <li>EVENTS</li>
      <li>PROFILES</li>
    </ul>
  </nav>
  <div class="search">type your keyword...
    <svg width="10" height="10" viewBox="0 0 10 10"><circle cx="6" cy="4" r="3" fill="none" stroke="#e0105a" stroke-width="1.3"/><line x1="3.8" y1="6.2" x2="1" y2="9" stroke="#e0105a" stroke-width="1.5"/></svg>
  </div>

  <section class="hero" role="img" aria-label="Featured photo of a performer in half drag make-up with red hair and jewels"></section>
  <div class="hero-caption">
    <h2>LOREM IPSUM TITLE</h2>
    <p>Neque elit sed ut imperdiet nisi. Proin condimentum fermentum nunc. Etiam pharetra, erat sed fermentum feugiat, velit mauris egestas quam, ut aliquam massa nisl quis neque. Suspendisse in orci enim.</p>
  </div>

  <aside class="sidebar">
    <h3 class="side-title">OUR LATEST TWEETS</h3>
    <div class="tweet"><b>@Someuser</b> Proin gravida nibh vel velit auctor aliquet. Aenean sollicitudin, lorem quis bibendum auctor, nisi elit consequat ipsum<time>09 Jun 2014</time></div>
    <div class="tweet"><b>@Someuser</b> Aenean sollicitudin, lorem quis bibendum auctor, nisi elit consequat ipsum<time>08 Jun 2014</time></div>
    <div class="tweet"><b>@Sample</b> Gravida nibh vel velit auctor aliquet lorem quis bibendum auctor, nisi elit consequat ipsum<time>07 Jun 2014</time></div>

    <div class="events">
      <h3 class="side-title">UPCOMING EVENTS</h3>
      <div class="event"><h4>09 Aug 2014</h4>Proin gravida nibh vel velit auctor aliquet. Aenean sollicitudin, lorem quis bibendum auctor, nisi elit consequat ipsum.<br>Location: <a>Nova Club</a></div>
      <div class="event"><h4>15 Aug 2014</h4>Etiam porta felis nec augue ultricies imperdiet. Nunc nibh nulla, dignissim a risus vel, cursus rhoncus nibh.<br>Location: <a>Metropole Club</a></div>
      <div class="event"><h4>30 Aug 2014</h4>Etiam porta felis nec augue ultricies imperdiet. Nunc nibh nulla, dignissim a risus vel, cursus rhoncus nibh.<br>Location: <a>Metropole Club</a></div>
    </div>
  </aside>

  <!-- column one -->
  <article class="card" style="left:204px;top:366px;width:130px;height:268px">
    <div class="video" role="img" aria-label="Video still of a singer" style="background:linear-gradient(135deg,#3b3b3b,#7a6a63 55%,#2a2a2a)">
      <div class="bar">Ivy Lorne - Becoming Iv...</div>
      <svg width="20" height="14" viewBox="0 0 20 14"><rect width="20" height="14" rx="3" fill="#1a1a1a"/><path d="M8 4l5 3-5 3z" fill="#fff"/></svg>
      <div class="controls">0:00 / 2:06</div>
    </div>
    <h3 class="post-title">NEW VIDEO FROM SOME EVENT (TUBELY)</h3>
    <div class="post-date">05 July 2014</div>
    <p class="post-body">Aenean sollicitudin, lorem quis bibendum auctor, nisi elit consequat ipsum, nec sagittis sem nibh id elit. Duis sed odio sit amet nibh vulputate cursus a sit amet mauris. Morbi accumsan ipsum velit.</p>
    <div class="post-meta">Comments: <a>12</a><br>Posted by: <a>Admin</a><br>Categories: <a>event</a></div>
  </article>

  <article class="card" style="left:204px;top:648px;width:130px;height:288px">
    <div class="placeholder" role="img" aria-label="Article picture"></div>
    <h3 class="post-title">PICTURE AND AN ARTICLE LEAD</h3>
    <div class="post-date">03 July 2014</div>
    <p class="post-body">Aenean sollicitudin, lorem quis bibendum auctor, nisi elit consequat ipsum, nec sagittis sem nibh id elit. Duis sed odio sit amet nibh vulputate cursus a sit amet mauris. Morbi accumsan ipsum velit.</p>
    <div class="post-meta">Comments: <a>12</a><br>Posted by: <a>Admin</a><br>Categories: <a>introducing</a></div>
  </article>

  <!-- column two -->
  <article class="card" style="left:350px;top:366px;width:131px;height:127px">
    <div class="pic blue" role="img" aria-label="Gallery picture">PICTURE</div>
  </article>
  <article class="card" style="left:350px;top:507px;width:131px;height:127px">
    <div class="pic teal" role="img" aria-label="Gallery picture">PICTURE</div>
  </article>
  <article class="card" style="left:350px;top:648px;width:131px;height:268px">
    <div class="video" role="img" aria-label="Video still of a nightclub stage with purple lights" style="background:linear-gradient(135deg,#3a1442,#b04a9c 50%,#241028)">
      <svg width="20" height="14" viewBox="0 0 20 14"><rect width="20" height="14" rx="3" fill="rgba(0,0,0,.6)"/><path d="M8 4l5 3-5 3z" fill="#fff"/></svg>
    </div>
    <h3 class="post-title">EMBEDDED VIDEO FROM VIDORA</h3>
    <div class="post-date">05 July 2014</div>
    <p class="post-body">Aenean sollicitudin, lorem quis bibendum auctor, nisi elit consequat ipsum, nec sagittis sem nibh id elit. Duis sed odio sit amet nibh vulputate cursus a sit amet mauris. Morbi accumsan ipsum velit.</p>
    <div class="post-meta">Comments: <a>12</a><br>Posted by: <a>Admin</a><br>Categories: <a>event</a></div>
  </article>

  <!-- column three -->
  <article class="card" style="left:498px;top:366px;width:131px;height:282px">
    <div class="placeholder" role="img" aria-label="Article picture"></div>
    <h3 class="post-title">PICTURE AND AN ARTICLE LEAD</h3>
    <div class="post-date">03 July 2014</div>
    <p class="post-body">Aenean sollicitudin, lorem quis bibendum auctor, nisi elit consequat ipsum, nec sagittis sem nibh id elit. Duis sed odio sit amet nibh vulputate cursus a sit amet mauris. Morbi accumsan ipsum velit.</p>
    <div class="post-meta">Comments: <a>12</a><br>Posted by: <a>Admin</a><br>Categories: <a>introducing</a></div>
  </article>
  <article class="card" style="left:498px;top:664px;width:131px;height:128px">
    <div class="pic blue" role="img" aria-label="Gallery picture">PICTURE</div>
  </article>

  <div class="load-more">Load more content</div>

  <footer class="site-footer">
    <div class="foot-col" style="left:56px">
      <h4 class="foot-title">USEFUL LINKS</h4>
      <ul class="foot-links"><li>Main Page</li><li>About Us</li><li>Blog</li><li>Photos</li><li>Events</li><li>Profiles</li></ul>
    </div>
    <div class="foot-col foot-text" style="left:155px;width:190px">
      <h4 class="foot-title">TEXT</h4>
      <p>The site will showcase the different drag queens of Manchester and provide an area for photography, video, social media feeds (such as zingo and Kinloop) as well as reviews of Drag queens to give the public a place to discuss shows or individuals.</p>
    </div>
    <div class="foot-col" style="left:350px">
      <h4 class="foot-title">LATEST PICTURES</h4>
      <div class="thumbs" role="img" aria-label="Latest gallery thumbnails"><span></span><span></span><span></span><span></span><span></span><span></span><span></span><span></span></div>
    </div>
    <div class="foot-col" style="left:546px">
      <h4 class="foot-title">SOCIALS</h4>
      <div class="socials">
        <div class="social one"><i></i>zingo</div>
        <div class="social two"><i></i>Kinloop</div>
        <div class="social three"><i></i>Tubely</div>
      </div>
    </div>
  </footer>
  <div class="bottom-bar"><span class="copy">© COPYRIGHT 2014 / VELVET STRUT</span><span class="policy">PRIVACY POLICY</span></div>

</div>
</body>
</html>
```